Business Card Design

We are an IT staffing and consulting company providing IT solutions and resources to our clients.

Industry/Entity Type

Business

Contact Information for Business Card

Ramesh Tulavarthi
Vice President

BrightNode Inc
48215 Harrowmere Court Square, suite 700
Ashburn, VA 20147
Direct: 571-555-0193
Mobile: 571-555-0147
Email: Ramesh@brightnodeinc.com
Fax: 703-555-0162
www.brightnodeinc.com

```html
<!DOCTYPE html>
<html lang="en">
<head>
<meta charset="utf-8">
<title>BrightNode Inc – Business Card</title>
<link href="https://fonts.googleapis.com/css2?family=Lato:wght@400;700;900&display=swap" rel="stylesheet">
<style>
  :root {
    --stage: #2b2b2b;
    --paper: #f7f7f7;
    --paper-shade: #e6e6e6;
    --brand-red: #a3141f;
    --brand-red-deep: #7e0d16;
    --ink: #222222;
    --service-ink: #1a0003;
    --white: #ffffff;
  }
  * { box-sizing: border-box; margin: 0; padding: 0; }
  html, body {
    width: 1200px; height: 873px; overflow: hidden;
    background: var(--stage);
    font-family: "Lato", sans-serif;
  }
  .card {
    position: absolute; left: 180px; top: 196px;
    width: 840px; height: 480px;
    border-radius: 22px; overflow: hidden;
    display: flex;
    box-shadow: 0 18px 40px rgba(0,0,0,.55);
  }
  .card__brand {
    width: 360px;
    background: linear-gradient(135deg, var(--white), var(--paper) 55%, var(--paper-shade));
    display: flex; flex-direction: column; justify-content: center; align-items: center;
    gap: 34px; padding-top: 20px;
  }
  .brand-name { font-weight: 900; font-size: 44px; color: var(--ink); letter-spacing: .5px; }
  .brand-url { font-weight: 700; font-size: 19px; color: var(--ink); letter-spacing: 1.5px; }
  .brand-url span { color: var(--brand-red); }
  .card__details {
    flex: 1; position: relative;
    background: linear-gradient(160deg, var(--brand-red), var(--brand-red-deep));
    padding: 30px 40px 24px 66px; color: var(--white);
  }
  .divider { position: absolute; top: 0; bottom: 0; width: 6px; background: var(--white); }
  .divider--outer { left: 8px; }
  .divider--inner { left: 22px; }
  .pointer { position: absolute; left: 30px; top: 42px; }
  .person__name { font-weight: 900; font-size: 27px; }
  .person__title { font-weight: 700; font-size: 16px; text-align: right; width: 300px; margin-top: -2px; }
  .contact { list-style: none; margin-top: 12px; font-size: 17px; line-height: 1.32; }
  .contact li { display: flex; align-items: center; gap: 14px; }
  .contact li.contact__address { align-items: flex-start; font-size: 14px; line-height: 1.3; margin-top: 2px; }
  .contact li.contact__address svg { margin-top: 2px; }
  .contact svg { width: 14px; height: 14px; flex: none; }
  .services__heading {
    display: block; margin: 6px 0 14px 92px;
    font-size: 15px; text-decoration: underline; letter-spacing: .5px;
  }
  .services { list-style: none; font-size: 15px; line-height: 1.5; text-transform: uppercase; }
  .services li { display: flex; align-items: center; gap: 12px; color: var(--service-ink); }
  .services li::before {
    content: ""; width: 12px; height: 12px; border-radius: 50%; background: var(--white); flex: none;
  }
</style>
</head>
<body>
  <article class="card">
    <section class="card__brand">
      <div class="brand-name">BrightNode</div>
      <div class="brand-url">www.<span>brightnodeinc</span>.com</div>
    </section>
    <section class="card__details">
      <span class="divider divider--outer"></span>
      <span class="divider divider--inner"></span>
      <svg class="pointer" width="18" height="20" viewBox="0 0 18 20"><polygon points="0,0 18,10 0,20" fill="#111"/></svg>
      <h1 class="person__name">Ramesh Tulavarthi</h1>
      <p class="person__title">Vice President</p>
      <ul class="contact">
        <li><svg viewBox="0 0 14 14"><path d="M1 5 Q7 0 13 5 L11 7 L9 5 L5 5 L3 7 Z M3 8 H11 V13 H3 Z" fill="#fff"/></svg>571-555-0193</li>
        <li><svg viewBox="0 0 14 14"><rect x="3" y="1" width="8" height="12" rx="1.5" fill="none" stroke="#fff" stroke-width="1.4"/></svg>571-555-0147</li>
        <li><svg viewBox="0 0 14 14"><rect x="1" y="5" width="12" height="8" fill="#fff"/><rect x="4" y="1" width="6" height="4" fill="none" stroke="#fff" stroke-width="1.4"/></svg>703-555-0162</li>
        <li><svg viewBox="0 0 14 14"><rect x="1" y="3" width="12" height="8" fill="#fff"/><path d="M1 3 L7 8 L13 3" fill="none" stroke="#a3141f" stroke-width="1.2"/></svg>Ramesh@brightnodeinc.com</li>
        <li class="contact__address"><svg viewBox="0 0 14 14"><path d="M7 1 C4 1 2.5 3.2 2.5 5.4 C2.5 8.6 7 13 7 13 C7 13 11.5 8.6 11.5 5.4 C11.5 3.2 10 1 7 1 Z" fill="#fff"/><circle cx="7" cy="5.4" r="1.7" fill="#a3141f"/></svg><span>48215 Harrowmere Court Square, suite 700<br>Ashburn, VA 20147</span></li>
      </ul>
      <span class="services__heading">OUR SERVICES</span>
      <ul class="services">
        <li>E-Commerce</li>
        <li>Data Mining</li>
        <li>Client Server</li>
        <li>Web Development</li>
        <li>Data Warehousing</li>
        <li>Groupware Technologies</li>
        <li>Quality Assurance &amp;</li>
        <li>Network Management Systems</li>
      </ul>
    </section>
  </article>
</body>
</html>
```